Lorvika.no is a new website about pedagogical entrepreneurship. It's main target group is teachers. The Fjellmark Institute for Classroom Media and the Nordvik Agency for Schools and Study are leading the project.

The web page is meant to show examples of how different methods of entrepreneurship can be used pedagogical in a learning environment. The page will also support the user with examples of different teaching programs and other examples of best practice.

Pedagogical entrepreneurship is not about business and men in suits. It's a method for learning. The focus in the design should be on school, education and new ways of learning.

The final product should be motivating and engaging, but at the same time governmental and serious. We are not looking for something "flashy" and corporate-looking, but a moderate, task-focused and clean design that state quality.

We need designs for three pages:
1 - frontpage
2 - subpage ("Metoder og undervisningsopplegg")
3 - subpage ("Smått-VERK i Brekkelia")

The interaction design for these three pages will be uploaded as an attachment.

We would like you to find inspiration in the following websites:
- www.gryvekst.no
- www.lavrek.no
- www.tovandstudio.com
- www.kvp.no
(more will be added)

Please use the attached logo, and feel free to use this as an inspiration for the rest of the design.

Target Market(s)

Teachers

Industry/Entity Type

Education

Requirements
Must have
• * Header with: Logo. Main navigation. Utility navigation. Search box.
* Footer
Should not have
• Images of men in suits.
Very strong graphical elements that stands out too much (we want it clean).

```html
<!DOCTYPE html>
<html lang="en">
<head>
<meta charset="utf-8">
<title>Lorvika.no – Entreprenørielle metoder i undervisningen</title>
<link rel="stylesheet" href="https://fonts.googleapis.com/css2?family=Arimo:ital,wght@0,400;0,700;1,700&display=swap">
<style>
:root{
  --navy:#0b4a7a;
  --navy-dark:#08355a;
  --sky:#7ea8c2;
  --sky-light:#a9c7da;
  --title-blue:#1a4f8a;
  --link-blue:#1f5b93;
  --orange:#f07d1a;
  --page:#ececec;
  --panel:#e3e3e3;
  --card:#f7f7f7;
  --text:#333;
  --muted:#555;
  --footer:#343434;
  --footer-text:#bdbdbd;
  --black:#0b0b0b;
  --white:#fff;
  --red:#c0121a;
}
*{box-sizing:border-box;margin:0;padding:0}
html,body{width:896px;height:1200px;overflow:hidden}
body{position:relative;background:var(--page);font-family:"Arimo",Arial,sans-serif;color:var(--text);font-size:9px}
a{color:inherit;text-decoration:none}
.abs{position:absolute}

/* header */
.site-header{position:absolute;left:0;top:0;width:896px;height:87px;background:var(--white)}
.utility-nav{left:413px;top:0;width:260px;height:14px;background:#2a2a2a;border-radius:0 0 4px 4px;color:#eee;font-size:8.5px;display:flex;justify-content:center;align-items:center;gap:6px}
.social{left:676px;top:4px;display:flex;gap:3px}
.social span{width:14px;height:14px;border-radius:2px;background:#5c8fb8}
.site-title{left:123px;top:20px;font-style:italic;font-weight:700;font-size:22px;line-height:24px;color:var(--title-blue)}
.site-title span{display:block;padding-left:28px}
.search{left:433px;top:28px;width:153px;height:18px;border:1px solid #bbb;background:#fff}
.search-btn{left:590px;top:27px;width:47px;height:19px;background:#222;color:#fff;font-size:9px;display:flex;align-items:center;justify-content:center}
.main-nav{left:360px;top:56px;width:416px;height:24px;background:var(--navy);border-radius:4px 4px 0 0;display:flex;color:#fff;font-size:9.5px}
.main-nav a{flex:auto;display:flex;align-items:center;justify-content:center;border-right:1px solid #2d6a98}
.main-nav a:last-child{border:0}

/* hero */
.hero-band{left:0;top:80px;width:896px;height:240px;background:linear-gradient(#8db3cb,var(--sky) 60%,#6b98b6)}
.hero{left:120px;top:91px;width:656px;height:240px;border-radius:6px 6px 0 0;overflow:hidden}
.hero svg{position:absolute;left:0;top:0}
.brand{left:24px;top:14px;display:flex;align-items:center;gap:8px;color:#fff;font-size:26px;font-weight:700}
.brand i{width:22px;height:22px;border-radius:50%;background:#fff}
.brand-tag{left:24px;top:45px;color:#cfe0ee;font-size:7px}
.hero-copy{left:8px;top:67px;width:355px;padding:12px 18px;background:rgba(255,255,255,.12)}
.hero-copy h1{font-size:19px;color:#fff;font-weight:700;line-height:22px}
.hero-copy p{font-size:16px;line-height:19px;color:#bcd8ee}
.learn-more{left:117px;top:180px;width:112px;height:30px;background:linear-gradient(#f9a34a,var(--orange));border:1px solid #c2590a;border-radius:3px;color:#222;font-weight:700;font-size:13px;display:flex;align-items:center;justify-content:center;gap:6px}
.learn-more b{width:16px;height:16px;border-radius:50%;background:#222;display:inline-block;position:relative}
.learn-more b:after{content:"";position:absolute;left:6px;top:4px;border-left:6px solid #fff;border-top:4px solid transparent;border-bottom:4px solid transparent}
.hero-photo{left:373px;top:16px;width:280px;height:193px;background:radial-gradient(circle at 50% 55%,#d9e6f1,#6f9cc4 60%,rgba(40,90,140,0) 75%)}

/* content */
.content{left:120px;top:349px;width:656px;height:624px;background:#fff;border:1px solid #ddd}
.features{left:128px;top:355px;width:640px;height:185px;background:var(--panel)}
.card{top:381px;width:193px;height:130px;background:var(--card);border:1px solid #d2d2d2;border-radius:4px;box-shadow:0 3px 5px rgba(0,0,0,.12)}
.card h2{margin:5px auto 0;width:140px;height:36px;background:linear-gradient(#fff,#e6e6e6);color:var(--title-blue);font-size:11px;text-align:center;display:flex;align-items:center;justify-content:center;line-height:13px}
.card .icon{position:absolute;left:18px;top:56px;width:40px;height:40px;border-radius:6px}
.card p,.card ul{position:absolute;left:66px;top:50px;width:120px;font-size:7.5px;line-height:9.5px;color:#333}
.card ul{list-style:none;top:56px}
.card li:before{content:"";display:inline-block;margin-right:5px;border-left:5px solid var(--orange);border-top:3px solid transparent;border-bottom:3px solid transparent}

.welcome{left:133px;top:553px;width:424px}
.welcome h2{font-size:12.5px;font-weight:400;color:#222;margin-bottom:12px}
.welcome p{font-size:8.2px;line-height:11px;margin-bottom:8px}

.get-started{left:132px;top:671px;width:425px;height:162px;background:#f3f3f3;border:1px solid #ccc}
.get-started h2{height:28px;background:linear-gradient(#fff,#e2e2e2);font-size:15px;padding:6px 10px;color:#222;border-bottom:1px solid #ccc}
.gs-col{position:absolute;top:36px;font-size:8px;line-height:18px}
.gs-col h3{font-size:9px;color:var(--title-blue);line-height:14px;margin-bottom:2px}
.gs-col a{display:block;text-decoration:underline;color:#222}

.widget{left:567px;width:200px;background:#eee;border:1px solid #ccc}
.widget h2{height:24px;background:linear-gradient(#e5e5e5,#cfcfcf);font-size:11px;color:#444;padding:5px 8px;position:relative}
.widget h2:after{content:"";position:absolute;right:6px;top:4px;width:16px;height:15px;background:#777;border-radius:2px}
.video{top:547px;height:189px}
.player{position:absolute;left:9px;top:34px;width:181px;height:145px;background:#222;border:1px solid #555}
.player-controls{position:absolute;left:0;bottom:0;width:100%;height:14px;background:#cfd6df}
.newsletter{top:747px;height:86px}
.newsletter h2{font-size:15px;color:#333}
.nl-box{position:absolute;left:6px;top:28px;width:186px;height:38px;background:#f7f7f7;border:1px solid #ccc;font-size:8px;padding:3px 6px}
.nl-input{position:absolute;left:30px;top:18px;width:97px;height:14px;border:1px solid #aaa;background:#fff}
.nl-submit{position:absolute;left:130px;top:18px;width:48px;height:14px;background:#444;color:#fff;font-size:7.5px;font-weight:700;display:flex;align-items:center;justify-content:center;border-radius:2px}
.nl-terms{position:absolute;left:6px;top:71px;font-size:7px}
.nl-terms i{display:inline-block;width:7px;height:7px;border:1px solid #888;margin-right:4px;vertical-align:-1px}
.nl-terms span{color:var(--red)}

.learnings{left:128px;top:840px;width:640px;height:133px;background:var(--panel)}
.learn-label{top:895px;font-size:10px;font-weight:700;color:#333;line-height:12px}
.arrow{top:886px;width:20px;height:40px;background:#fafafa;border:1px solid #bbb}
.strip{left:220px;top:856px;width:456px;height:104px;background:#fff;box-shadow:0 2px 6px rgba(0,0,0,.2)}
.thumb{position:absolute;top:12px;width:77px}
.thumb div{height:45px}
.thumb p{font-size:8px;line-height:10px;margin-top:4px;color:#222}

/* footer */
.site-footer{left:0;top:980px;width:896px;height:193px;background:var(--footer)}
.f-brand{left:198px;top:62px;display:flex;align-items:center;gap:7px;color:#c8d9e8;font-size:16px;font-weight:700}
.f-brand i{width:18px;height:18px;border-radius:50%;background:#5f97c8}
.f-col{position:absolute;top:13px;font-size:8px;color:var(--footer-text);line-height:18.5px}
.f-col h3{font-size:9.5px;color:#fff;margin-bottom:12px;line-height:14px}
.f-col h4{font-size:8px;color:#fff;line-height:18px}
.f-col .more{color:#fff;text-decoration:underline}
.f-rule{left:185px;top:1008px;width:580px;height:1px;background:#444}
.copyright{left:0;top:1173px;width:896px;height:27px;background:var(--black);color:#ddd;font-size:9px;display:flex;align-items:center;justify-content:center}
</style>
</head>
<body>

<header class="site-header">
  <nav class="abs utility-nav"><a>Best Practice schools</a>|<a>Lorvikameter</a>|<a>About Lorvika.no</a></nav>
  <div class="abs social" aria-label="Social links"><span></span><span></span><span></span><span></span></div>
  <div class="abs site-title">Enterprenerielle metoder<span>i undervisiningen</span></div>
  <div class="abs search"></div>
  <a class="abs search-btn">Search</a>
  <nav class="abs main-nav">
    <a>Home</a><a>Why Lorvika</a><a>Testimonials</a><a>Methods</a><a>News</a><a>Blog</a><a>Contact Us</a>
  </nav>
</header>

<div class="abs hero-band"></div>
<section class="abs hero">
  <svg width="656" height="240" viewBox="0 0 656 240">
    <defs>
      <radialGradient id="heroGlow" cx="0.7" cy="0.3" r="0.8">
        <stop offset="0" stop-color="#2e7fc0"/><stop offset="1" stop-color="#0a3b66"/>
      </radialGradient>
    </defs>
    <path d="M0 0H656V220Q328 250 0 222Z" fill="url(#heroGlow)"/>
    <path d="M0 222Q328 250 656 220V240H0Z" fill="#6b98b6"/>
  </svg>
  <div class="abs brand"><i></i>Lorvika</div>
  <div class="abs brand-tag">Entreprenørielle metoder i undervisningen</div>
  <div class="abs hero-copy">
    <h1>Pedagogical entrepreneurship works.</h1>
    <p>Lorem ipsum dolor sit amet, consecteur adipiscing elit, sed do euismod tempor incidunt ut labore et dolore magna aliqua...</p>
  </div>
  <a class="abs learn-more">Learn More <b></b></a>
  <div class="abs hero-photo" role="img" aria-label="Photo of students relaxing on blue bean bags with laptops and books"></div>
</section>

<main>
  <div class="abs content"></div>
  <div class="abs features"></div>

  <article class="abs card" style="left:140px">
    <h2>What is Pedagogical<br>Entrepreneurship?</h2>
    <div class="icon" role="img" aria-label="Red question mark cube illustration" style="background:#c8202a"></div>
    <p>Lorem ipsum dolor sit amet, con secteur, adipiscing elit. Set diam nonumy euismod incidunt ut labo re et dolore magna aliquam. Ut e nim ad minim veniam, quis nos-trud exercitation.</p>
  </article>
  <article class="abs card" style="left:349px">
    <h2>Methods And<br>Teaching Plans</h2>
    <div class="icon" role="img" aria-label="Colourful illustration of a figure with books" style="background:#d33a8a"></div>
    <ul><li>Lorem ipsum dolor sit amet.</li><li>Lorem ipsum dolor sit amet.</li><li>Lorem ipsum dolor sit amet.</li><li>Lorem ipsum dolor sit amet.</li></ul>
  </article>
  <article class="abs card" style="left:559px">
    <h2>Good Examples<br>/Best Practices</h2>
    <svg class="icon" viewBox="0 0 40 40" role="img" aria-label="Award badge"><path d="M14 24 10 38 17 34 20 38 22 26ZM26 24 30 38 23 34 20 38 18 26Z" fill="#b01822"/><circle cx="20" cy="16" r="13" fill="#c89a3c"/><circle cx="20" cy="16" r="9" fill="#8a2a20"/></svg>
    <p>Lorem ipsum dolor sit amet, consec teteur adipiscing elit.<br>Lorem ipsum dolor sit amet.<br>Lorem ipsum dolor sit amet, consec teteur adipiscing elit.<br>Lorem ipsum dolor sit amet.</p>
  </article>

  <section class="abs welcome">
    <h2>WELCOME to LORVIKA</h2>
    <p>Duis aute irure in reprehenderit in volutpate velit esse cullum dolore eu fugiat nulla pariatur. Excepteur sint occae cat cupidatat non proident, sunt in culpa qui officia deserunt mollit animit est laborum.</p>
    <p><b>Lorem ipsum dolor sit amet</b>, consectetur adipiscing elit. Sed do euismod tempor incidunt utlabore et dolore mag na aliquam. Ut enim ad minim veniam, quis nostrud exercitation ullamcolaboris nisi ut aliquip ex ea commodo consequat. Duis aute irure dolor in reprehenderit in voluptat velit esse cillum dolore eu fugiat nulla patatur.</p>
  </section>

  <section class="abs get-started">
    <h2>GET Started</h2>
    <div class="gs-col" style="left:10px">
      <h3>Methods</h3>
      <a>Cafe Pedagogik</a><a>Elevbedrift</a><a>Gundercamp</a><a>Story line</a><a>REAL</a><a>See more</a>
    </div>
    <div class="gs-col" style="left:169px">
      <h3>Teaching Plans</h3>
      <a>Teaching Plan Tittle</a><a>Teaching Plan Tittle</a><a>Teaching Plan Tittle</a><a>Teaching Plan Tittle</a><a>See more</a>
    </div>
  </section>

  <aside class="abs widget video">
    <h2>Featured Video</h2>
    <div class="player">
      <svg width="181" height="131" viewBox="0 0 181 131"><path d="M84 55v20l16-10Z" fill="#000"/></svg>
      <div class="player-controls"></div>
    </div>
  </aside>

  <aside class="abs widget newsletter">
    <h2>Newsletter</h2>
    <div class="nl-box">Receive Our Monthly Newsletter<div style="position:absolute;left:6px;top:20px">Email</div><div class="nl-input"></div><div class="nl-submit">SUBMIT</div></div>
    <div class="nl-terms"><i></i>I understand with the <span>terms and conditions</span></div>
  </aside>

  <section class="abs learnings">
  </section>
  <svg class="abs arrow" style="left:133px;border-radius:0 20px 20px 0;transform:scaleX(-1)" viewBox="0 0 20 40"><path d="M7 13l7 7-7 7" stroke="#777" stroke-width="3" fill="none"/></svg>
  <div class="abs learn-label" style="left:163px">Featured<br>Learnings</div>
  <div class="abs strip">
    <div class="thumb" style="left:9px"><div role="img" aria-label="Photo of a class of children" style="background:linear-gradient(#6fa0c8,#5b8a4a)"></div><p>Lorem ipsum dolor sit Amet.</p></div>
    <div class="thumb" style="left:100px"><div role="img" aria-label="Photo of children playing with toys" style="background:linear-gradient(#d8b04a,#3f7fb8)"></div><p>Lorem ipsum dolor sit Amet.</p></div>
    <div class="thumb" style="left:189px"><div role="img" aria-label="Photo of a student at a board" style="background:linear-gradient(#2f6fb0,#b9d0e6)"></div><p>Lorem ipsum dolor sit Amet.</p></div>
    <div class="thumb" style="left:279px"><div role="img" aria-label="Photo of students in a classroom" style="background:linear-gradient(#9aa9b8,#5f6d7c)"></div><p>Lorem ipsum dolor sit Amet.</p></div>
    <div class="thumb" style="left:368px"><div role="img" aria-label="Photo of a chalkboard with formulas" style="background:linear-gradient(#3c5f78,#8fa6b6)"></div><p>Lorem ipsum dolor sit Amet.</p></div>
  </div>
  <div class="abs learn-label" style="left:683px">Featured<br>Learnings</div>
  <svg class="abs arrow" style="left:742px;border-radius:20px 0 0 20px" viewBox="0 0 20 40"><path d="M7 13l7 7-7 7" stroke="#777" stroke-width="3" fill="none"/></svg>
</main>

<footer class="abs site-footer">
  <div class="abs f-brand"><i></i>Lorvika</div>
  <div class="f-col" style="left:344px">
    <h3>Pedagocical entrepreneurship</h3>
    <div>What is Pedagogical enterpreneurship?</div><div>Science</div><div>Best practice school</div><div>Lorvikameter</div><div>About Lorvika.no</div>
  </div>
  <div class="f-col" style="left:550px">
    <h3>Methods</h3>
    <div>Storyline</div><div>REAL</div><div>Cafe Pedagogikk</div><div class="more">See more</div>
    <h4>Teaching Plans</h4><div>Tittle</div><div>Tittle</div><div class="more">See more</div>
  </div>
  <div class="f-col" style="left:662px">
    <h3>Gode Eksemplar</h3>
    <div>Smått-VERK at Brekkelia school</div><div>Smått-VERK at Brekkelia school</div><div>Smått-VERK at Brekkelia school</div><div class="more">See more</div>
  </div>
</footer>
<div class="abs f-rule"></div>
<div class="abs copyright">Copyright &copy; 2012, Lorvika.com. All rights resreved.</div>

</body>
</html>
```